Flyer design for Trail Beside Outback Trips

We need a new flyer for our tour business. Sketch hive produced a great flyer for us 4 years ago but it is time to update. We have had a price increase that needs to be reflected but we have noticed an issue with our current marketing.
Our tour is a "tagalong" tour which means you follow in your own vehicle. Unfortunately most people associate "tagalong" with 4wd (Four wheel drive vehicles). This is not the case for our tour which can be done in ANY type of vehicle. We need to get across at first glance that this tour is available to all vehicle types. We also need to stress that there is NOT MUCH DRIVING. We cover around 20km total of very easy driving. We go from point of interest to point of interest.
We want our customers to feel that this tour will be a better option than selecting a bus type tour because they use their own vehicle. Our option is also MUCH cheaper than bus options but provides a premium product. It's "cheap" but not cheap if you understand.
I will upload our previous flyer so you have an idea of what we do and how we have been presenting it. We are currently single sided DL but do not mind if we go into double sided DL if you feel that will enable you to share more information. Our price is $50 and half price for kids (as per old flyer)
Some things to remember when trying to appeal to our customer:
Choose a design that clearly communicates that our tagalong tour is suitable for all types of vehicles. For example, "Vehicle-Friendly Tagalong Tour" or "All-Vehicle Tagalong Tour".
Use clear language: Avoid using terms like "off-road" or "4x4" that may imply that our tour is only suitable for certain types of vehicles. Instead, use language that is inclusive and clearly communicates that all vehicles are welcome.
Include photos and videos of a variety of vehicles: This will show potential customers that our tagalong tour is not limited to four-wheel drive vehicles and that any type of vehicle can participate.
Highlight the benefits of a tagalong tour over a bus tour: Emphasise the flexibility and freedom that a tagalong tour offers, as well as the opportunity to explore off-the-beaten-path destinations that are not accessible by bus.
By incorporating these elements into your product presentation, you can avoid confusion and clearly communicate that our tagalong tour is suitable for any type of vehicle, while also highlighting the unique benefits of this type of tour.
Along with the emphasis on all vehicles you need to be clear about what we offer on the tour.
- The excitement of an opal mine tour with an award winning guide and opal miner.
- The wonder of an underground home and discovering how people live in an underground environment.
- Driving through the opal mining area for a close up view of the field.
- Our EXCLUSIVE opal cutting and polishing demonstration.
- The adventure of looking for your own opal.
For further information visit our web site "http://trailbeside.outbackway.example". Check our facebook page "https://www.facebook.com/trailbesideoutbacktrips". Search Seekora for "Coober Pedy", Trail beside Outback Coober Pedy" or "Coober Pedy Opal mining" to source images of our town and opals.
PLEASE ALSO FIND SOMEWHERE TO SAY "FREE UNPOWERED CAMPING AT TALMO'S WITH ALL TOURS AS WELL AS DISCOUNTS ON POWERED CAMPING" and make this stand out somehow. (http://stay-belowgrid.example.au)

Target Market(s)

18 to 80

Industry/Entity Type

Tourism

Font styles to use
Serif

Colors

Designer to choose colors to be used in the design.

Requirements
Must have
• Eye catching images and attention grabbing headlines
Nice to have
• Modern design.
Should not have
• References to 4wd or buses.

```html
<!DOCTYPE html>
<html lang="en">
<head>
<meta charset="utf-8">
<title>Trail Beside Outback Trips – Tagalong Flyer</title>
<link href="https://fonts.googleapis.com/css2?family=Poppins:wght@400;500;600;700;800&display=swap" rel="stylesheet">
<style>
  :root {
    --orange: #f07f0c;
    --orange-soft: #f9bd7a;
    --charcoal: #2c2c2c;
    --ink: #262626;
    --paper: #ffffff;
    --mist: #efefef;
    --rule: #c9c9c9;
    --stage: #ffffff;
  }
  * { box-sizing: border-box; margin: 0; padding: 0; }
  html, body { width: 765px; height: 1200px; overflow: hidden; background: var(--stage); }
  body { font-family: "Poppins", sans-serif; color: var(--ink); position: relative; }

  .flyer {
    position: absolute; top: 239px; width: 340px; height: 722px; overflow: hidden;
    box-shadow: 0 4px 14px rgba(0,0,0,.18);
  }
  .flyer--front { left: 30px; background: var(--paper); }
  .flyer--back { left: 395px; background: var(--mist); }
  .flyer > * { position: absolute; }
  .shapes { left: 0; top: 0; width: 340px; height: 722px; }

  .brand-badge {
    border-radius: 50%; background: var(--orange);
    display: flex; align-items: center; justify-content: center;
    color: #fff; font-weight: 600; text-align: center; line-height: 1.1;
  }
  .flyer--front .brand-badge { left: 110px; top: 26px; width: 118px; height: 118px; font-size: 17px; }
  .flyer--back .brand-badge { left: 101px; top: 19px; width: 136px; height: 136px; font-size: 19px; }

  .tour-photo {
    left: 0; top: 0; width: 340px; height: 262px;
    background: linear-gradient(180deg, #5a8fd0 0%, #a9c9ee 38%, #d9d7cf 55%, #9b8a72 75%, #7d6a55 100%);
  }

  .title-tagalong {
    left: 0; width: 340px; top: 298px; text-align: center;
    font-size: 51px; font-weight: 700; letter-spacing: -0.5px; color: var(--ink); line-height: 1;
  }
  .title-sub {
    left: 0; width: 340px; top: 368px; text-align: center;
    font-size: 22px; font-weight: 700; color: #fff; line-height: 1.05;
  }

  .feature-strip { left: 0; top: 428px; width: 340px; height: 44px; display: flex; }
  .feature-strip__easy {
    width: 149px; background: var(--orange-soft); display: flex; align-items: center;
    justify-content: center; gap: 8px; font-weight: 700; font-size: 12px; line-height: 1.05; color: var(--ink);
  }
  .feature-strip__easy svg { width: 20px; height: 20px; }
  .feature-strip__detail {
    flex: 1; background: var(--charcoal); color: #fff; font-size: 9.5px; font-weight: 600;
    display: flex; align-items: center; padding-left: 12px; line-height: 1.3;
  }

  .welcome { left: 30px; top: 484px; font-size: 13px; line-height: 1; color: var(--ink); }
  .welcome strong { display: block; font-size: 21px; font-weight: 600; margin-top: 1px; }
  .welcome-rule { left: 149px; top: 484px; width: 1px; height: 46px; background: var(--orange); }
  .welcome-note { left: 161px; top: 484px; width: 160px; font-size: 9px; line-height: 1.3; color: var(--ink); }
  .welcome-note b { font-weight: 600; }

  .price-pill {
    left: 43px; top: 542px; width: 254px; height: 38px; border-radius: 19px;
    background: var(--charcoal); color: #fff; text-align: center; padding-top: 5px;
  }
  .price-pill__main { font-size: 14px; font-weight: 700; line-height: 1.05; }
  .price-pill__kids { font-size: 8px; font-weight: 500; color: var(--orange); letter-spacing: 2.3px; }

  .web-frame { left: 40px; width: 260px; height: 26px; border: 1px solid var(--orange); border-top: none; }
  .web-frame::before, .web-frame::after {
    content: ""; position: absolute; top: 0; height: 1px; width: 28px; background: var(--orange);
  }
  .web-frame::before { left: 0; } .web-frame::after { right: 0; }
  .web-frame__label {
    position: absolute; top: -6px; left: 0; width: 100%; text-align: center; font-size: 9px; color: var(--ink);
  }
  .web-frame__url {
    position: absolute; top: 8px; left: 0; width: 100%; text-align: center;
    font-size: 10.5px; font-weight: 700; color: #c75e00; background: transparent;
  }
  .flyer--front .web-frame { top: 604px; }
  .flyer--back .web-frame { left: 22px; width: 296px; top: 603px; }
  .flyer--back .web-frame::before, .flyer--back .web-frame::after { width: 34px; }
  .flyer--back .web-frame__label { font-size: 10px; top: -7px; }
  .flyer--back .web-frame__url { font-size: 12px; }

  .follow-band {
    left: 0; top: 639px; width: 340px; height: 23px; background: #c65f00;
    display: flex; align-items: center; justify-content: center; gap: 6px;
    color: #fff; font-size: 6.6px; font-weight: 600;
  }
  .follow-band .dot { width: 6px; height: 6px; border-radius: 50%; background: #fff; display: inline-block; vertical-align: -0.5px; margin: 0 2px; }
  .follow-band .sep { width: 1px; height: 10px; background: #fff; }
  .footer-url {
    left: 0; top: 663px; width: 340px; height: 59px; background: var(--charcoal);
    color: #fff; font-size: 15px; font-weight: 500; display: flex; align-items: center; justify-content: center;
  }

  .camping-head {
    left: 0; width: 340px; top: 162px; text-align: center; color: #fff; font-weight: 800; line-height: 0.95;
  }
  .camping-head__main { font-size: 26px; }
  .camping-head__where { font-size: 16px; font-weight: 700; margin-top: 3px; }
  .camping-head__note {
    display: inline-block; background: var(--charcoal); font-size: 7.5px; font-weight: 600;
    padding: 2px 8px; margin-top: 3px;
  }

  .offers-title {
    left: 0; width: 340px; top: 314px; text-align: center; font-size: 13px; font-weight: 600; color: #c75e00;
  }
  .offers-dots { left: 0; width: 340px; top: 329px; text-align: center; font-size: 8px; color: var(--orange); letter-spacing: 1px; line-height: 1; }
  .offers-intro {
    left: 30px; width: 280px; top: 338px; text-align: center; font-size: 9.5px; line-height: 1.3; color: var(--ink);
  }
  .we-offer { left: 28px; top: 381px; display: flex; align-items: center; gap: 8px; }
  .we-offer__lead { font-size: 23px; font-weight: 600; color: var(--ink); line-height: 1; }
  .we-offer__tag { background: var(--charcoal); color: #fff; font-size: 16px; letter-spacing: 1.2px; padding: 2px 12px; line-height: 1.3; }

  .offer-list { left: 22px; top: 418px; width: 296px; list-style: none; }
  .offer-list li {
    display: flex; gap: 9px; align-items: center; font-size: 9.8px; line-height: 1.25;
    padding: 4px 0 6px; border-bottom: 1px solid var(--rule); min-height: 34px;
  }
  .offer-list li:last-child { border-bottom: none; }
  .offer-list svg { flex: 0 0 16px; width: 16px; height: 16px; }
</style>
</head>
<body>

<section class="flyer flyer--front" aria-label="Flyer front">
  <div class="tour-photo" role="img" aria-label="Photo of a row of varied cars and utes parked on outback ground with tour guests beside them under a blue sky"></div>
  <svg class="shapes" viewBox="0 0 340 722">
    <path d="M0,292 Q170,256 340,292 L340,428 L0,428 Z" fill="var(--orange)"/>
    <path d="M0,250 Q170,214 340,250 L340,296 Q170,260 0,296 Z" fill="var(--charcoal)"/>
    <path d="M0,273 Q170,237 340,273" fill="none" stroke="#fff" stroke-width="1.6" stroke-dasharray="11 8"/>
  </svg>
  <div class="brand-badge">Trail<br>Beside</div>

  <h1 class="title-tagalong">tagalong</h1>
  <p class="title-sub">VEHICLE-FRIENDLY<br>TAGALONG TOUR</p>

  <div class="feature-strip">
    <div class="feature-strip__easy">
      <svg viewBox="0 0 20 20" aria-hidden="true"><circle cx="10" cy="10" r="8" fill="none" stroke="var(--ink)" stroke-width="2.4"/><circle cx="10" cy="10" r="2" fill="var(--ink)"/><path d="M3,9 H17" stroke="var(--ink)" stroke-width="2"/></svg>
      <span>NOT MUCH<br>DRIVING</span>
    </div>
    <div class="feature-strip__detail">We cover around 20km total<br>of very easy driving.</div>
  </div>

  <p class="welcome">All vehicles are<strong>Welcome</strong></p>
  <div class="welcome-rule"></div>
  <p class="welcome-note">Tagalong tour is not limited to four-wheel drive vehicles and <b>that any type of vehicle can participate.</b></p>

  <div class="price-pill">
    <div class="price-pill__main">OUR PRICE IS $50 PER PERSON</div>
    <div class="price-pill__kids">HALF PRICE FOR KIDS</div>
  </div>

  <div class="web-frame">
    <span class="web-frame__label">For further information visit our web site</span>
    <span class="web-frame__url">http://trailbeside.outbackway.example</span>
  </div>

  <div class="follow-band">
    <span>Follow <i class="dot"></i> @trailbesideoutbacktrips</span>
    <i class="sep"></i>
    <span>Follow Seekora Trail beside Outback Coober Pedy</span>
  </div>
  <div class="footer-url">www.trailbeside.outbackway.example</div>
</section>

<section class="flyer flyer--back" aria-label="Flyer back">
  <svg class="shapes" viewBox="0 0 340 722">
    <path d="M0,104 Q170,150 340,104 L340,258 Q170,280 0,258 Z" fill="var(--orange)"/>
    <path d="M0,100 Q170,146 340,100 L340,112 Q170,156 0,116 Z" fill="var(--charcoal)"/>
    <path d="M0,252 Q170,274 340,252 L340,292 Q170,314 0,292 Z" fill="var(--charcoal)"/>
    <path d="M0,272 Q170,294 340,272" fill="none" stroke="#fff" stroke-width="1.6" stroke-dasharray="11 8"/>
  </svg>
  <div class="brand-badge">Trail<br>Beside</div>

  <h2 class="camping-head">
    <div class="camping-head__main">FREE UNPOWERED<br>CAMPING</div>
    <div class="camping-head__where">AT TALMO'S WITH ALL TOURS</div>
    <span class="camping-head__note">AS WELL AS DISCOUNTS ON POWERED CAMPING</span>
  </h2>

  <h3 class="offers-title">Tagalong Tour Offers</h3>
  <div class="offers-dots">••••••</div>
  <p class="offers-intro">Flexibility and freedom , as well as the opportunity to explore off-the-beaten-path destinations that are not accessible by bus.</p>

  <div class="we-offer">
    <span class="we-offer__lead">WE OFFER</span>
    <span class="we-offer__tag">ON THE TOUR</span>
  </div>

  <ul class="offer-list">
    <li><svg viewBox="0 0 16 16" aria-hidden="true"><circle cx="7" cy="9" r="6" fill="none" stroke="var(--orange)" stroke-width="1.5"/><path d="M4,8.5 L7,12 L15,2" fill="none" stroke="var(--orange)" stroke-width="2.2"/></svg>The excitement of an opal mine tour with an award winning guide and opal miner.</li>
    <li><svg viewBox="0 0 16 16" aria-hidden="true"><circle cx="7" cy="9" r="6" fill="none" stroke="var(--orange)" stroke-width="1.5"/><path d="M4,8.5 L7,12 L15,2" fill="none" stroke="var(--orange)" stroke-width="2.2"/></svg>The wonder of an underground home &amp; discovering how people live in an underground environment.</li>
    <li><svg viewBox="0 0 16 16" aria-hidden="true"><circle cx="7" cy="9" r="6" fill="none" stroke="var(--orange)" stroke-width="1.5"/><path d="M4,8.5 L7,12 L15,2" fill="none" stroke="var(--orange)" stroke-width="2.2"/></svg>Driving through the opal mining area for a close up view of the field.</li>
    <li><svg viewBox="0 0 16 16" aria-hidden="true"><circle cx="7" cy="9" r="6" fill="none" stroke="var(--orange)" stroke-width="1.5"/><path d="M4,8.5 L7,12 L15,2" fill="none" stroke="var(--orange)" stroke-width="2.2"/></svg>Our EXCLUSIVE opal cutting and polishing demonstration.</li>
    <li><svg viewBox="0 0 16 16" aria-hidden="true"><circle cx="7" cy="9" r="6" fill="none" stroke="var(--orange)" stroke-width="1.5"/><path d="M4,8.5 L7,12 L15,2" fill="none" stroke="var(--orange)" stroke-width="2.2"/></svg>The adventure of looking for your own opal.</li>
  </ul>

  <div class="web-frame">
    <span class="web-frame__label">For further information visit our web site</span>
    <span class="web-frame__url">http://trailbeside.outbackway.example</span>
  </div>

  <div class="follow-band">
    <span>Follow <i class="dot"></i> @trailbesideoutbacktrips</span>
    <i class="sep"></i>
    <span>Follow Seekora Trail beside Outback Coober Pedy</span>
  </div>
  <div class="footer-url">www.trailbeside.outbackway.example</div>
</section>

</body>
</html>
```